Startup Drone Platform Company business card

We are needing a business card design for our employees. We are a startup drone platform. We are looking for a business card that has our logo on one side, with the employee/company details on the opposite side. We are looking for something that is very eye catching, modern, and bold.

Target Market(s)

This will target both drone pilots and drone businesses, along with all the industries that could utilize drone services (aerial video, aerial photos, inspections, 3d mapping, etc).

Industry/Entity Type

Business

```html
<!DOCTYPE html>
<html lang="en">
<head>
<meta charset="utf-8">
<title>Skylift Rentals – Business Card</title>
<link href="https://fonts.googleapis.com/css2?family=Montserrat:wght@500&family=Roboto:wght@400&display=swap" rel="stylesheet">
<style>
  :root {
    --page-bg: #e9e9e7;
    --card-top: #1c1d1e;
    --card-bottom: #262728;
    --card-back: #202122;
    --accent: #3ab5c0;
    --text-light: #ffffff;
    --text-muted: #b9b9b9;
  }
  html, body {
    margin: 0;
    padding: 0;
    width: 1200px;
    height: 934px;
    overflow: hidden;
    background: var(--page-bg);
  }
  .canvas {
    position: relative;
    width: 1200px;
    height: 934px;
  }
  .card {
    position: absolute;
    left: 288px;
    width: 626px;
    height: 358px;
    border-radius: 24px;
    overflow: hidden;
  }
  .card--front {
    top: 78px;
    background: var(--card-bottom);
  }
  .card--back {
    top: 497px;
    background: radial-gradient(ellipse at 50% 45%, #262728 0%, var(--card-back) 70%);
  }
  .front-header {
    position: absolute;
    left: 0; top: 0;
    width: 100%;
    height: 160px;
    background: var(--card-top);
  }
  .front-header__notch {
    position: absolute;
    left: 44px;
    top: 160px;
    width: 0; height: 0;
    border-left: 14px solid transparent;
    border-right: 14px solid transparent;
    border-top: 14px solid var(--card-top);
  }
  .wordmark {
    font-family: "Montserrat", sans-serif;
    font-weight: 500;
    color: var(--text-light);
    letter-spacing: 0.42em;
    text-transform: uppercase;
    white-space: nowrap;
  }
  .front-header .wordmark {
    position: absolute;
    left: 0; right: 0;
    top: 58px;
    text-align: center;
    font-size: 30px;
    padding-left: 0.42em;
  }
  .person {
    position: absolute;
    left: 51px;
    top: 202px;
    font-family: "Roboto", sans-serif;
    display: flex;
    align-items: center;
    white-space: nowrap;
  }
  .person__name {
    color: var(--accent);
    font-size: 24px;
    text-transform: uppercase;
  }
  .person__divider {
    width: 2px;
    height: 24px;
    background: var(--text-light);
    margin: 0 12px;
  }
  .person__title {
    color: var(--text-light);
    font-size: 16px;
    margin-top: 4px;
  }
  .contacts {
    position: absolute;
    left: 49px;
    top: 250px;
    margin: 0;
    padding: 0;
    list-style: none;
    font-family: "Roboto", sans-serif;
    font-size: 17px;
    color: var(--text-muted);
  }
  .contacts li {
    display: flex;
    align-items: center;
    height: 21.3px;
  }
  .contacts svg {
    width: 16px;
    height: 16px;
    margin-right: 10px;
    flex: none;
  }
  .back-mark {
    position: absolute;
    left: 0; right: 0;
    top: 96px;
    text-align: center;
  }
  .back-mark__dot {
    display: block;
    margin: 0 auto 34px;
    width: 120px;
    height: 120px;
    border-radius: 50%;
    border: 3px solid var(--accent);
    box-sizing: border-box;
  }
  .back-mark .wordmark {
    display: block;
    font-size: 21px;
    line-height: 30px;
    padding-left: 0.42em;
  }
</style>
</head>
<body>
<main class="canvas">

  <section class="card card--front" aria-label="Business card front">
    <header class="front-header">
      <div class="wordmark">Skylift Rentals</div>
      <div class="front-header__notch"></div>
    </header>

    <div class="person">
      <span class="person__name">Maren Castell</span>
      <span class="person__divider"></span>
      <span class="person__title">CEO / Director</span>
    </div>

    <ul class="contacts">
      <li>
        <svg viewBox="0 0 16 16" aria-hidden="true"><rect x="4" y="1" width="8" height="14" rx="1.5" fill="none" stroke="var(--accent)" stroke-width="1.5"/><circle cx="8" cy="12.5" r="0.9" fill="var(--accent)"/></svg>
        555-014-2387
      </li>
      <li>
        <svg viewBox="0 0 16 16" aria-hidden="true"><rect x="1.5" y="4" width="13" height="9" fill="var(--accent)"/><path d="M1.5 4 L8 9 L14.5 4" fill="none" stroke="var(--card-bottom)" stroke-width="1.2"/></svg>
        info@skyliftrentals.com
      </li>
      <li>
        <svg viewBox="0 0 16 16" aria-hidden="true"><circle cx="8" cy="8" r="6.5" fill="none" stroke="var(--accent)" stroke-width="1.5"/><path d="M1.5 8 H14.5 M8 1.5 C5 5 5 11 8 14.5 M8 1.5 C11 5 11 11 8 14.5" fill="none" stroke="var(--accent)" stroke-width="1.1"/></svg>
        www.skyliftrentals.com
      </li>
      <li>
        <svg viewBox="0 0 16 16" aria-hidden="true"><path d="M8 1.5 L15 8 H12.8 V14.5 H9.6 V10.5 H6.4 V14.5 H3.2 V8 H1 Z" fill="var(--accent)"/></svg>
        48 Orchard Lane, 7 Bld, USA, 400210
      </li>
    </ul>
  </section>

  <section class="card card--back" aria-label="Business card back">
    <div class="back-mark">
      <span class="back-mark__dot"></span>
      <span class="wordmark">Skylift</span>
      <span class="wordmark">Rentals</span>
    </div>
  </section>

</main>
</body>
</html>
```